Business Card Needed for Crafter of Pottery, Jewelry and Artwork

Calling all designers in search of an artistic challenge.

I need a new business card design for my pottery, jewelry and artwork business, Woven Glass and Tide, based in Vancouver BC.

I would like a card that is bright and inviting and preferably incorporates my logo and a sample of photos of my work while having a clean fresh look. The following contact details would preferably be included on the card as well:
• Helena Pikeworth
• Designer
• Phone: 604.555.0172
• Email: Designer@WovenGlassandTide.example
• Website: www.WovenGlassandTide.example
• Blog: www.ShapingHillside.example

The logo is attached in two color schemes in both Vector and Source formats. On past cards I’ve also included photos of my work. By including photos of the work the pieces are showcased and it catches people’s eye and prompts them to pick up the card and look at it more closely. For example, if I leave a stack in a coffee shop I want people to be drawn to the card, to pick it up and get a sense of the my product lines. Please feel free to pull photos of my work directly off of my website. If you need photos with higher pixels please let me know and I’ll email them directly to you. The website background is bffbda (191, 251, 218). I would like the business cards to match the feel of the website for consistency but the cards do not need to use the exact same colors. My website and current business card are predominantly turquoise shades. The background uses stripes provided by the website template. I don’t know the exact colors of the stripes.

My current business card is attached to show the use of photos in a design. Please note that I am not thrilled with my own design and am looking for variations and completely new designs. This example is not meant to be used as a template or starting point.

Here is some background surrounding my company:
WGT offers one of a kind jewelry, pottery, artwork and leather bags each designed with a twist. The pottery varies from rustic every day functional ware to raku artwork. The jewelry ranges from simple sterling every day pieces to multimedia pieces incorporating stone, metal, ceramics and fabric. The artwork is multimedia, typically acrylic paired with a natural element such as bark. All the bags are leather with reworked kimono fabric or patterned silk lining.

Feel free to check out my website to get a flavour for my work and the color scheme I've used on marketing materials so far. www.wovenglassandtide.example
Updates

Thank you to everyone who has submitted a design so far. I hope everyone has received some helpful feedback.

I'm going to post a survey to customers and friends asking for their votes. If you have new designs to submit please try to get them in by Saturday March 30 at noon so that I can include it in the survey launch.

Thank you

Target Market(s)

Females aged 25-65 interested in one of a kind functional pottery and jewelry.

Industry/Entity Type

Coffee Shop

Requirements
Must have
• Contact information, website, blog
Nice to have
• Logo, photos

```html
<!DOCTYPE html>
<html lang="en">
<head>
<meta charset="utf-8">
<title>Woven Glass and Tide — Business Card</title>
<link href="https://fonts.googleapis.com/css2?family=Questrial&display=swap" rel="stylesheet">
<style>
  :root {
    --teal: #1fa89b;
    --teal-soft: #4fbdb1;
    --paper: #ffffff;
    --backdrop: #eceeed;
    --pottery-a: #e9edf0;
    --pottery-b: #d9dfe2;
    --earring-a: #e4e6f0;
    --earring-b: #d3d6e4;
    --burlap-a: #cfcbc2;
    --burlap-b: #b7b2a7;
  }
  * { box-sizing: border-box; margin: 0; padding: 0; }
  html, body {
    width: 1079px;
    height: 1200px;
    overflow: hidden;
    background: var(--backdrop);
    font-family: "Questrial", "Helvetica Neue", Arial, sans-serif;
  }
  .card {
    position: absolute;
    left: 89px;
    width: 900px;
    height: 514px;
    background: var(--paper);
    box-shadow: 0 6px 22px rgba(0,0,0,0.12);
    overflow: hidden;
  }
  .card--front { top: 57px; }
  .card--back  { top: 628px; }

  .brand-mark {
    position: absolute;
    border: 3px solid var(--teal);
    border-radius: 50%;
    display: flex;
    align-items: center;
    justify-content: center;
    color: var(--teal);
    letter-spacing: 0.06em;
  }
  .dots {
    position: absolute;
    display: flex;
    gap: 14px;
  }
  .dots span {
    width: 5px; height: 5px; border-radius: 50%;
    background: var(--teal);
  }

  /* front */
  .card--front .brand-mark {
    left: 392px; top: 96px; width: 116px; height: 116px;
    font-size: 30px;
  }
  .front-name {
    position: absolute;
    left: 0; right: 0; top: 238px;
    text-align: center;
    color: var(--teal);
    font-size: 32px;
    font-weight: 400;
    font-variant: small-caps;
    letter-spacing: 0.04em;
  }
  .card--front .dots { left: 433px; top: 312px; }

  /* back: photo band */
  .photo { position: absolute; top: 0; }
  .photo--pottery {
    left: 0; width: 306px; height: 322px;
    background: linear-gradient(160deg, var(--pottery-a), var(--pottery-b));
  }
  .photo--drop-earrings {
    left: 309px; width: 321px; height: 268px;
    background: linear-gradient(170deg, var(--earring-a), var(--earring-b));
  }
  .photo--cluster-earrings {
    left: 633px; width: 267px; height: 268px;
    background: linear-gradient(150deg, var(--burlap-a), var(--burlap-b));
  }
  .rule { position: absolute; background: var(--teal); }
  .rule--band    { left: 306px; top: 268px; width: 594px; height: 3px; }
  .rule--pottery { left: 0; top: 322px; width: 309px; height: 3px; }
  .rule--split1  { left: 306px; top: 0; width: 3px; height: 325px; }
  .rule--split2  { left: 630px; top: 0; width: 3px; height: 270px; }

  .card--back .brand-mark {
    left: 320px; top: 288px; width: 84px; height: 84px;
    font-size: 22px;
  }
  .rule--divider { left: 420px; top: 288px; width: 2px; height: 82px; }

  .identity {
    position: absolute;
    left: 436px; top: 290px;
    color: var(--teal);
  }
  .identity__name {
    font-size: 27px;
    font-weight: 400;
    font-variant: small-caps;
    letter-spacing: 0.04em;
    line-height: 1.15;
    white-space: nowrap;
  }
  .identity__role {
    margin-top: 2px;
    font-size: 21px;
    font-variant: small-caps;
    color: var(--teal-soft);
    letter-spacing: 0.04em;
    line-height: 1.15;
  }

  .contact {
    position: absolute;
    display: flex;
    align-items: center;
    gap: 10px;
    color: var(--teal);
    font-size: 16px;
    font-variant: small-caps;
    letter-spacing: 0.03em;
    white-space: nowrap;
  }
  .contact svg { flex: none; }
  .contact--phone { right: 30px; top: 292px; font-size: 18px; }
  .contact--email { right: 30px; top: 392px; }
  .contact--web   { left: 22px; top: 398px; }
  .contact--blog  { left: 22px; top: 432px; }

  .card--back .dots { left: 612px; top: 446px; }
</style>
</head>
<body>

<section class="card card--front" aria-label="Card front">
  <div class="brand-mark">WGT</div>
  <h1 class="front-name">Helena Pikeworth</h1>
  <div class="dots"><span></span><span></span><span></span></div>
</section>

<section class="card card--back" aria-label="Card back">
  <div class="photo photo--pottery" role="img" aria-label="Photo of two glazed white and cream ceramic pots"></div>
  <div class="photo photo--drop-earrings" role="img" aria-label="Photo of drop earrings with navy, orange and purple stones hanging on a driftwood branch"></div>
  <div class="photo photo--cluster-earrings" role="img" aria-label="Photo of pink and aqua beaded cluster earrings on burlap"></div>

  <div class="rule rule--split1"></div>
  <div class="rule rule--split2"></div>
  <div class="rule rule--band"></div>
  <div class="rule rule--pottery"></div>

  <div class="brand-mark">WGT</div>
  <div class="rule rule--divider"></div>

  <div class="identity">
    <h2 class="identity__name">Helena Pikeworth</h2>
    <p class="identity__role">Designer</p>
  </div>

  <p class="contact contact--phone">
    <svg width="14" height="22" viewBox="0 0 14 22" aria-hidden="true">
      <rect x="1" y="1" width="12" height="20" rx="2" fill="none" stroke="currentColor" stroke-width="1.6"/>
      <line x1="5" y1="17.5" x2="9" y2="17.5" stroke="currentColor" stroke-width="1.6"/>
    </svg>
    604.555.0172
  </p>
  <p class="contact contact--email">
    <svg width="20" height="14" viewBox="0 0 20 14" aria-hidden="true">
      <rect x="0" y="0" width="20" height="14" fill="currentColor"/>
      <polyline points="0,0 10,8 20,0" fill="none" stroke="#fff" stroke-width="1.4"/>
    </svg>
    Designer@WovenGlassandTide.example
  </p>
  <p class="contact contact--web">
    <svg width="16" height="16" viewBox="0 0 16 16" aria-hidden="true">
      <circle cx="8" cy="8" r="7" fill="none" stroke="currentColor" stroke-width="1.4"/>
      <ellipse cx="8" cy="8" rx="3" ry="7" fill="none" stroke="currentColor" stroke-width="1.2"/>
      <line x1="1" y1="8" x2="15" y2="8" stroke="currentColor" stroke-width="1.2"/>
    </svg>
    www.WovenGlassandTide.example
  </p>
  <p class="contact contact--blog">
    <svg width="16" height="16" viewBox="0 0 16 16" aria-hidden="true">
      <circle cx="8" cy="8" r="7" fill="currentColor"/>
    </svg>
    www.ShapingHillside.example
  </p>

  <div class="dots"><span></span><span></span><span></span></div>
</section>

</body>
</html>
```